Design einer Angebotsmappe
Zielgruppe
Wir sind ein Handwerksbetrieb im Bereich Elektrotechnik.
Wir betreuen private Haushalte, Gewerbekunden oder Architekten.
Mehr über uns : www.kessler-brandau.de
Aufgabenstellung
Es soll das Design für eine Angebotsmappe erstellt werden. Die Mappe soll einen sehr hochwertigen und professionellen Eindruck beim Kunden machen.
Unser Logo soll auf der Vorderseite platziert werden und mit partiellen UV Lack in Szene gesetzt werden.
Alles andere ist Ihrer Kreativität überlassen.
-An geeigneter Stelle soll auf unsere Profile bei Instagram & Facebook hingewiesen werden mit passenden Icon und Accountname.
-Sowie ein Hinweis auf unsere Internetseite www.kessler-brandau.de
Zu beachten sind die Druckvorgaben im Anhang

```html
<!DOCTYPE html>
<html lang="de">
<head>
<meta charset="utf-8">
<title>Angebotsmappe – Kessler &amp; Brandau Elektrotechnik</title>
<link rel="stylesheet" href="https://fonts.googleapis.com/css2?family=Montserrat:wght@600&family=Open+Sans:wght@400&display=swap">
<style>
  :root {
    --stage: #dedede;
    --paper-top: #e9ecef;
    --paper-bottom: #f1f2f3;
    --brand-blue: #2c8fc9;
    --text-grey: #5b6670;
    --teal: #3aa9b3;
    --teal-light: #47b8c2;
    --teal-dark: #1f7c83;
    --net-blue-1: #cfe2f3;
    --net-blue-2: #a9c9ef;
    --white: #ffffff;
  }
  html, body {
    margin: 0;
    width: 1200px;
    height: 1200px;
    overflow: hidden;
    background: var(--stage);
  }
  .canvas {
    position: relative;
    width: 1200px;
    height: 1200px;
  }
  .folder-cover {
    position: absolute;
    left: 232px;
    top: 80px;
    width: 736px;
    height: 1040px;
    background: linear-gradient(180deg, var(--paper-top), var(--paper-bottom));
    box-shadow: 0 12px 30px rgba(0,0,0,0.12);
    overflow: hidden;
  }
  .cover-art {
    position: absolute;
    inset: 0;
    width: 736px;
    height: 1040px;
  }
  .brand {
    position: absolute;
    left: 70px;
    top: 130px;
    display: flex;
    flex-direction: column;
    align-items: flex-start;
    gap: 8px;
  }
  .brand-row {
    display: flex;
    align-items: center;
    gap: 12px;
  }
  .brand-dot {
    width: 18px;
    height: 18px;
    border-radius: 50%;
    background: var(--brand-blue);
  }
  .brand-name {
    font-family: "Montserrat", sans-serif;
    font-weight: 600;
    font-size: 26px;
    letter-spacing: 1px;
    text-transform: uppercase;
    color: var(--brand-blue);
  }
  .brand-trade {
    font-family: "Open Sans", sans-serif;
    font-size: 12px;
    letter-spacing: 4px;
    text-transform: uppercase;
    color: var(--text-grey);
    padding: 2px 0 0 30px;
    border-top: 1px solid var(--text-grey);
    width: 240px;
  }
  .document-title {
    position: absolute;
    right: 56px;
    top: 812px;
    font-family: "Open Sans", sans-serif;
    font-weight: 400;
    font-size: 40px;
    letter-spacing: 8px;
    color: var(--white);
  }
</style>
</head>
<body>
<div class="canvas">
  <div class="folder-cover">
    <svg class="cover-art" viewBox="0 0 736 1040" xmlns="http://www.w3.org/2000/svg">
      <defs>
        <linearGradient id="net-fade" x1="0" y1="0" x2="1" y2="1">
          <stop offset="0" stop-color="var(--net-blue-1)" stop-opacity="0.55"/>
          <stop offset="1" stop-color="var(--net-blue-2)" stop-opacity="0.9"/>
        </linearGradient>
      </defs>
      <path class="network-graphic" role="img" aria-label="Abstrakte Netzwerkgrafik mit Punkten und Linien in hellen Blautönen"
            d="M300 0 H736 V1040 H300 V760 H380 A420 420 0 0 0 520 220 L300 0 Z"
            fill="url(#net-fade)"/>
      <polygon class="band-lower" points="0,880 360,880 280,940 0,940" fill="var(--teal)"/>
      <polygon class="band-wedge" points="250,940 440,800 736,800 736,872 440,872" fill="var(--teal-dark)"/>
      <polygon class="band-upper" points="440,800 736,800 736,872 400,872" fill="var(--teal-light)"/>
    </svg>
    <div class="brand">
      <div class="brand-row">
        <span class="brand-dot"></span>
        <span class="brand-name">Kessler &amp; Brandau</span>
      </div>
      <div class="brand-trade">Elektrotechnik</div>
    </div>
    <div class="document-title">ANGEBOT</div>
  </div>
</div>
</body>
</html>
```